依頼詳細
法人化にすることによって名刺のデザインを一新したく、シンプルだけど一目でrn事務所とわかる名刺にしたいです。ロゴはございますので、そのロゴを活用して作っていただきたい
記載項目
表面はシンプルに、表面、裏面に住所や電話番号などのデザインはお任せでしたいとおもいます。
一級建築士事務所
株式会社rn森下建築事務所
代表取締役 森下拓真
〒806-0091北九州市八幡西区松尾2丁目5-8ルミナ松尾3F
Tel 093-548-3190 Fax 093-548-3195
E-mail:arc@rn-morishita-sekkei.com
http://www.rn-morishita-sekkei.com

希望イメージ
シンプル 複雑
単色 カラフル
暗い 明るい
日常 高級
遊び心 厳粛
未来的 伝統的
女性的 男性的
希望する色
納品ファイル
• 高解像度JPG (.jpg)
• イラストレーター形式 (.ai)
• フォトショップ形式 (.psd)
補足説明
今までで13件の提案がございましたが、どれも同じようなデザインで、目を引くようなのがございません。もっと斬新的なデザインを希望します。
RN MORISHITA ARCHITECT DESIGN STUDIO を追加で書き込んでもらいたいです

シンプルかつシャープなイメージが気に入りました

このたびは「株式会社rn森下建築事務所」の法人化設立の名刺を沢山の方から提案していただきありがとうございました。どれもこれも良くて選ぶのに時間がかかってしまい申し訳ありませんでした。悩んだ結果、当選させていただきました。本当にありがとうございました

```html
<!DOCTYPE html>
<html lang="ja">
<head>
<meta charset="utf-8">
<title>株式会社rn森下建築事務所 名刺デザイン</title>
<link href="https://fonts.googleapis.com/css2?family=Noto+Sans+JP:wght@400;500;700&display=swap" rel="stylesheet">
<style>
  :root {
    --bg-center: #cfeef2;
    --bg-mid: #6fc3cf;
    --bg-edge: #1f7f99;
    --frame: #2b6f88;
    --card-front: #1b1b1d;
    --card-back: #6a6a6a;
    --text-light: #ffffff;
    --text-soft: #ececec;
    --line-red: #d62a2a;
    --line-blue: #2f6fc7;
    --photo-light: #e9e1d3;
    --photo-mid: #b7a58a;
    --photo-dark: #5d5448;
  }
  * { margin: 0; padding: 0; box-sizing: border-box; }
  html, body { width: 778px; height: 1200px; overflow: hidden; }
  body {
    position: relative;
    font-family: "Noto Sans JP", sans-serif;
    background: radial-gradient(ellipse at 50% 50%, var(--bg-center) 0%, var(--bg-mid) 45%, var(--bg-edge) 100%);
    border: 3px solid var(--frame);
  }
  .card { position: absolute; box-shadow: 0 3px 8px rgba(0,0,0,.35); }

  /* Front */
  .card-front {
    left: 83px; top: 83px; width: 632px; height: 359px;
    background: var(--card-front);
  }
  .front-photo {
    position: absolute; left: 302px; top: 16px; width: 322px; height: 135px;
    background: linear-gradient(160deg, var(--photo-light) 0%, var(--photo-mid) 55%, var(--photo-dark) 100%);
  }
  .front-mark { position: absolute; left: 34px; top: 85px; }
  .rule { position: absolute; left: 0; width: 632px; height: 4px; }
  .rule-red { top: 154px; background: var(--line-red); }
  .rule-blue { top: 166px; background: var(--line-blue); }
  .front-info {
    position: absolute; right: 18px; top: 258px;
    color: var(--text-light); text-align: right;
    font-size: 12px; line-height: 19px; font-weight: 500;
  }
  .front-info .name {
    font-size: 24px; line-height: 30px; font-weight: 500;
    letter-spacing: .12em; margin-top: 4px;
  }

  /* Brand name stand-in */
  .brand-name {
    font-family: "Noto Sans JP", sans-serif; font-weight: 700;
    font-size: 50px; line-height: 1; color: var(--text-light);
    white-space: nowrap;
  }

  /* Back */
  .card-back {
    left: 122px; top: 520px; width: 458px; height: 637px;
    background: var(--card-back);
  }
  .back-mark { position: absolute; left: 0; width: 100%; top: 200px; text-align: center; }
  .back-info {
    position: absolute; left: 34px; top: 392px;
    color: var(--text-light);
  }
  .back-info .office { font-size: 16px; line-height: 26px; font-weight: 500; }
  .back-info .contact { margin-top: 28px; font-size: 11px; line-height: 22px; color: var(--text-soft); }
</style>
</head>
<body>

  <section class="card card-front">
    <div class="front-photo" role="img" aria-label="明るい住宅インテリアの室内写真"></div>
    <div class="front-mark">
      <span class="brand-name">rn事務所</span>
    </div>
    <div class="rule rule-red"></div>
    <div class="rule rule-blue"></div>
    <div class="front-info">
      <p>一級建築士事務所</p>
      <p>株式会社rn森下建築事務所</p>
      <p>代表取締役</p>
      <p class="name">森下 拓真</p>
    </div>
  </section>

  <section class="card card-back">
    <div class="back-mark">
      <span class="brand-name">rn事務所</span>
    </div>
    <div class="back-info">
      <p class="office">一級建築士事務所</p>
      <p class="office">株式会社rn森下建築事務所</p>
      <div class="contact">
        <p>〒806-0091</p>
        <p>北九州市八幡西区松尾2丁目5-8ルミナ松尾3F</p>
        <p>Tel 093-548-3190　Fax 093-548-3195</p>
        <p>E-mail:arc@rn-morishita-sekkei.com</p>
        <p>HP http://www.rn-morishita-sekkei.com</p>
      </div>
    </div>
  </section>

</body>
</html>
```